WordPress Site Design and Code for Technology Consulting Startup

We need a WordPress design and code to a new site on Nimbo Vault. We have the logo and colors ready. The site will be a brochure site with a CONTACT page that contains a form that the prospective client fills out. The other pages would be ABOUT / SERVICES (3 option drop-down) / SUPPORT. The site should be appropriate for an IT Consulting / IT Managed Services / IT Project Management services in the Chicago area.

Target Market(s)

Across small, medium, large businesses.

Industry/Entity Type

Technology, network infrastructure, IT.

Coding

Coded - Design and coding required

Number of Pages Required

5+ page

Requirements
Nice to have
• I prefer mid-modern / simple / art deco / minimalist.

```html
<!DOCTYPE html>
<html lang="en">
<head>
<meta charset="utf-8">
<title>Corvane IT Consulting</title>
<link href="https://fonts.googleapis.com/css2?family=Montserrat:wght@400;500;600;700;800&display=swap" rel="stylesheet">
<style>
:root{
  --teal:#1b8fa6;
  --teal-dark:#0f5f70;
  --orange:#f47b20;
  --ink:#0e1a22;
  --text:#333b40;
  --light-blue:#dcedf1;
  --peach:#fbe3d3;
  --grey:#c9c9c9;
  --white:#ffffff;
  --btn-grad:linear-gradient(90deg,#0f5f70 0%,#12323d 55%,#f47b20 100%);
}
*{box-sizing:border-box;margin:0;padding:0}
html,body{width:1200px;height:4372px;overflow:hidden}
body{position:relative;background:var(--white);font-family:'Montserrat',sans-serif;color:var(--text)}
.abs{position:absolute}
.btn{position:absolute;display:flex;align-items:center;justify-content:center;border-radius:20px;font-weight:700;font-size:15px;color:var(--white);background:var(--btn-grad);text-decoration:none}
.btn--outline{background:var(--white);color:var(--ink);border:2px solid var(--orange)}
.btn--teal{background:var(--teal)}
.btn--orange{background:var(--orange)}
.photo{position:absolute}

/* header */
.hero-blob-blue{left:-230px;top:-420px;width:900px;height:880px;border-radius:50%;background:linear-gradient(160deg,#cfe5eb,#eef6f8 70%,#ffffff)}
.hero-blob-peach{left:760px;top:-300px;width:220px;height:760px;border-radius:0 0 200px 120px;background:linear-gradient(180deg,#fde9dc,#fff6f0)}
.logo{left:29px;top:25px;display:flex;flex-direction:column;align-items:center;gap:6px}
.logo__mark{width:40px;height:40px;background:var(--teal)}
.logo__name{font-weight:700;font-size:28px;letter-spacing:2px;color:var(--ink)}
.nav{left:662px;top:43px;display:flex;gap:0;font-weight:700;font-size:15px;color:var(--ink)}
.nav span{position:absolute;white-space:nowrap}
.phone-btn{left:1005px;top:36px;width:170px;height:34px;font-size:15px}

/* hero */
.hero-title{left:626px;top:205px;color:var(--ink);font-weight:700}
.hero-title .kicker{font-size:19px;color:var(--orange);font-weight:600;display:block;margin-bottom:6px}
.hero-title .line{display:block;font-size:56px;line-height:65px}
.hero-title .line--teal{color:var(--teal)}

/* welcome */
.welcome{left:131px;top:786px;width:430px}
.kicker-sm{font-size:13px;font-weight:600;color:var(--orange);display:flex;align-items:center;gap:22px}
.kicker-sm i{display:block;width:32px;height:3px;background:linear-gradient(90deg,var(--orange),var(--ink))}
.welcome h2{font-size:36px;line-height:42px;color:var(--ink);margin-top:18px;font-weight:700}
.welcome .lead{font-size:13px;font-weight:600;color:var(--orange);margin-top:28px}
.welcome p{font-size:14px;line-height:18.5px;margin-top:14px}
.feature{position:absolute;width:180px;font-size:14px;line-height:18px}
.feature b{display:flex;align-items:center;gap:8px;font-size:13px;color:var(--ink);margin-bottom:9px;margin-left:-24px}
.feature b i{display:block;width:14px;height:14px;background:linear-gradient(135deg,var(--orange) 50%,var(--teal) 50%)}

/* services */
.services-band{left:87px;top:1442px;width:1019px;height:581px;background:linear-gradient(90deg,var(--light-blue) 0 45%,#ffffff 45% 55%,var(--peach) 55%)}
.services-title{left:129px;top:1436px;font-weight:700;font-size:28px;line-height:32px;color:var(--ink)}
.services-title .teal{color:var(--teal)}
.card{position:absolute;top:1566px;width:306px;height:457px;background:var(--white);border:6px solid;border-image:linear-gradient(160deg,var(--orange),var(--ink) 70%,var(--orange)) 1}
.card--teal{border-image:linear-gradient(160deg,var(--teal),var(--ink) 75%,var(--orange)) 1}
.card__img{position:absolute;left:2px;top:2px;right:2px;height:207px}
.card h3{position:absolute;left:19px;top:238px;font-size:18px;font-weight:700;color:var(--ink)}
.card p{position:absolute;left:19px;top:270px;width:260px;font-size:14.5px;line-height:18.5px}
.card .btn{left:18px;top:373px;width:124px;height:31px}

/* pricing */
.center{left:0;width:1200px;text-align:center}
.pricing-kicker{top:2110px;font-size:19px;font-weight:600;color:var(--orange)}
.pricing-title{top:2150px;font-size:27px;font-weight:700;color:var(--ink)}
.pricing-title .teal{color:var(--teal)}
.pricing-lead{left:272px;top:2200px;width:656px;text-align:center;font-size:14.5px;line-height:18.5px}
.plan{position:absolute;border:3px solid;border-image:linear-gradient(90deg,var(--teal),var(--orange)) 1;background:var(--white);text-align:center}
.plan--pro{border:none;background:linear-gradient(160deg,var(--teal) 15%,#8d9a84 55%,var(--orange) 80%);color:var(--white)}
.plan__pill{margin:0 auto;width:230px;height:34px;border-radius:17px;background:var(--light-blue);font-weight:700;font-size:15px;color:var(--ink);display:flex;align-items:center;justify-content:center}
.plan--pro .plan__pill{background:var(--white)}
.plan__price{font-size:40px;font-weight:700;color:var(--ink);margin-top:18px;line-height:46px}
.plan__price sup{font-size:18px;vertical-align:top;position:relative;top:4px}
.plan__price small{font-size:18px;color:var(--orange)}
.plan--pro .plan__price,.plan--pro .plan__price small{color:var(--white)}
.plan h4{font-size:16px;font-weight:700;color:var(--ink);margin-top:8px}
.plan--pro h4{color:var(--white)}
.plan ul{list-style:none;font-size:12px;line-height:25px;margin-top:6px}
.plan--pro ul{color:#eaf3f4}
.plan__scroll{position:absolute;width:4px;border-radius:2px;background:linear-gradient(180deg,var(--orange) 30%,#d6d6d6 30%)}
.plan--pro .plan__scroll{background:linear-gradient(180deg,var(--teal) 25%,#ffffff 25%)}
.plan .btn{left:50%;transform:translateX(-50%);width:124px;height:31px}

/* cta */
.cta-band{left:0;top:2899px;width:1200px;height:334px;background:linear-gradient(90deg,#d5e9ee 0%,#dcdcdc 55%,#fbe1cf 100%)}
.cta h2{position:absolute;left:125px;top:2940px;font-size:38px;line-height:45px;font-weight:700;color:var(--ink)}
.cta p{position:absolute;left:124px;top:3052px;width:375px;font-size:14.5px;line-height:18.5px}

/* contact */
.contact-frame{left:248px;top:3437px;width:652px;height:492px;background:var(--white);border:6px solid;border-image:linear-gradient(90deg,var(--teal),var(--ink) 60%,var(--orange)) 1}
.contact-kicker{top:3472px;font-size:13px;font-weight:600;color:var(--orange)}
.contact-title{top:3495px;font-size:36px;font-weight:700;color:var(--ink)}
.field{position:absolute;height:34px;border:1.5px solid #9aa0a4;background:var(--white);font-size:14px;color:#a5aaad;padding:8px 12px;font-family:inherit}
.field--area{height:120px}

/* footer */
.footer{left:0;top:4068px;width:1200px;height:304px;background:#000;color:#e6e6e6}
.fcol{position:absolute;top:4120px;font-size:12.5px;line-height:22px}
.fcol h5{font-size:19px;font-weight:700;color:var(--white);margin-bottom:14px}
.fcol .ico{display:flex;gap:14px;align-items:flex-start}
.fcol svg{flex:none;margin-top:3px}
.footer-bar{left:0;top:4320px;width:1200px;height:1px;background:#444}
.footer-logo{left:165px;top:4321px;width:263px;height:51px;background:linear-gradient(90deg,var(--teal),var(--orange));display:flex;align-items:center;justify-content:center;gap:10px;font-weight:700;font-size:26px;color:var(--white);letter-spacing:1px}
.footer-logo i{display:block;width:22px;height:22px;background:var(--white)}
.copyright{left:755px;top:4340px;font-size:12px;color:#e6e6e6}
.copyright u{color:var(--white)}
</style>
</head>
<body>

<!-- header & hero -->
<div class="abs hero-blob-blue"></div>
<div class="abs hero-blob-peach"></div>
<div class="abs" role="img" aria-label="Faint circuit board line pattern" style="left:0;top:640px;width:560px;height:680px;background:radial-gradient(ellipse at 30% 50%,#eef2f4,rgba(255,255,255,0) 70%)"></div>

<div class="abs logo"><span class="logo__mark"></span><span class="logo__name">CORVANE</span></div>
<nav class="abs nav">
  <span style="left:0">HOME</span>
  <span style="left:66px">ABOUT</span>
  <span style="left:139px">SERVICES</span>
  <span style="left:234px">CONTACT</span>
</nav>
<a class="btn phone-btn">
  <svg width="15" height="15" viewBox="0 0 24 24" fill="#fff" style="margin-right:8px"><path d="M6.6 10.8c1.4 2.8 3.8 5.1 6.6 6.6l2.2-2.2c.3-.3.7-.4 1-.2 1.1.4 2.3.6 3.6.6.6 0 1 .4 1 1V20c0 .6-.4 1-1 1C10.6 21 3 13.4 3 4c0-.6.4-1 1-1h3.5c.6 0 1 .4 1 1 0 1.3.2 2.5.6 3.6.1.3 0 .7-.2 1z"/></svg>555 010 2040</a>

<div class="abs" style="left:187px;top:153px;width:285px;height:320px;background:var(--orange);clip-path:polygon(0 0,100% 0,85% 40%,100% 100%,0 100%)"></div>
<div class="abs" style="left:387px;top:416px;width:212px;height:280px;background:linear-gradient(180deg,var(--teal),var(--teal-dark))"></div>
<div class="abs" style="left:190px;top:399px;width:12px;height:203px;background:var(--ink)"></div>
<div class="abs" style="left:574px;top:260px;width:9px;height:96px;background:var(--grey)"></div>
<div class="abs" style="left:217px;top:197px;width:336px;height:465px;border:6px solid;border-image:linear-gradient(135deg,var(--teal),var(--orange)) 1;background:#fff"></div>
<div class="photo" role="img" aria-label="Young man wearing a virtual reality headset in a neon-lit room" style="left:225px;top:205px;width:320px;height:449px;background:linear-gradient(160deg,#3b2a7a,#6a3fb0 40%,#1c2a55 80%,#c0632c)"></div>

<div class="abs hero-title">
  <span class="kicker">CORVANE IT CONSULTING</span>
  <span class="line">IT PROJECT</span>
  <span class="line line--teal">MANAGEMENT</span>
  <span class="line">SERVICES</span>
</div>
<a class="btn" style="left:624px;top:433px;width:150px;height:31px">Discover More</a>
<a class="btn btn--outline" style="left:786px;top:433px;width:129px;height:31px">Get a quote</a>
<div class="abs" role="img" aria-label="Orange hatched decorative blob" style="left:976px;top:411px;width:166px;height:158px;border-radius:48% 52% 40% 60%/40% 45% 55% 60%;background:#fbd7bd;transform:rotate(-12deg)"></div>

<!-- welcome -->
<div class="abs welcome">
  <div class="kicker-sm">WELCOME TO CORVANE <i></i></div>
  <h2>Best IT Technology Services you can Trust</h2>
  <div class="lead">The professional approach to Technology.</div>
  <p>It is a long established fact that a reader will be distracted by the readable content of a page when looking at its layout. The point of using Lorem Ipsum is that it has a more-or-less normal distribution of letters, as opposed to using 'Content here, content here', making it look like readable English</p>
</div>
<div class="feature" style="left:155px;top:1098px"><b><i></i>Project Management</b>It is a long established fact that a reader will be distracted.</div>
<div class="feature" style="left:367px;top:1098px"><b><i></i>Project Framework</b>It is a long established fact that a reader will be distracted.</div>
<a class="btn" style="left:131px;top:1212px;width:124px;height:32px">See More</a>

<div class="abs" role="img" aria-label="Orange hatched circle decoration" style="left:1018px;top:801px;width:100px;height:124px;border-radius:50%;background:#fcdcc6"></div>
<div class="photo" role="img" aria-label="Team meeting around a long conference table with laptops" style="left:585px;top:772px;width:484px;height:450px;border-radius:62% 38% 45% 55%/35% 55% 45% 65%;background:linear-gradient(150deg,#8a99a6,#b38157 45%,#d49563 70%,#6c5d56)"></div>
<div class="abs" style="left:607px;top:1061px;width:126px;height:128px;border-radius:50%;background:radial-gradient(circle at 30% 30%,var(--teal),var(--ink) 70%)"></div>

<!-- services -->
<div class="abs services-band"></div>
<svg class="abs" style="left:87px;top:1442px" width="1019" height="581" viewBox="0 0 1019 581">
  <polygon points="0,0 180,0 450,180 300,580 0,580" fill="#c7e0e7" opacity=".6"/>
  <polygon points="1019,0 800,0 540,210 700,580 1019,580" fill="#f9d3bb" opacity=".6"/>
</svg>
<div class="abs services-title">OUR<br><span class="teal">PROFESSIONAL</span><br>SERVICES</div>
<a class="btn" style="left:921px;top:1494px;width:126px;height:30px">See More</a>

<div class="card card--teal" style="left:127px">
  <div class="card__img" role="img" aria-label="People working at computers in an office" style="background:linear-gradient(150deg,#5b4a3e,#a0764e 50%,#3c3f4a)"></div>
  <h3>PROJECT MANAGEMENT</h3>
  <p>It is a long established fact that a reader will be distracted by the readable content of a page when looking</p>
  <a class="btn btn--teal">See More</a>
</div>
<div class="card" style="left:448px">
  <div class="card__img" role="img" aria-label="Glowing plasma ball on a dark background" style="background:radial-gradient(circle at 55% 45%,#d94a8c,#5a2a6e 30%,#111 65%)"></div>
  <h3>PROJECT FRAMEWORK</h3>
  <p>It is a long established fact that a reader will be distracted by the readable content of a page when looking</p>
  <a class="btn btn--teal">See More</a>
</div>
<div class="card card--teal" style="left:767px">
  <div class="card__img" role="img" aria-label="Desktop computer and tablet on a white desk" style="background:linear-gradient(160deg,#f1f3f5,#c9d3dc 60%,#e6e8ea)"></div>
  <h3>PROJECT CONTROLING</h3>
  <p>It is a long established fact that a reader will be distracted by the readable content of a page when looking</p>
  <a class="btn btn--teal">See More</a>
</div>

<!-- pricing -->
<div class="abs center pricing-kicker">PRICING PLANS</div>
<div class="abs center pricing-title">Our exciting <span class="teal">packages</span> that fulfill your need</div>
<p class="abs pricing-lead">We have fantastic and carefully bundled packages in store for you that are easy on your pocket and deliver huge value. Incase you need a personalized package for your campaign, we can deliver that as well.</p>

<div class="plan" style="left:126px;top:2315px;width:288px;height:455px;padding-top:32px">
  <div class="plan__pill">Basic Combo Package</div>
  <div class="plan__price"><sup>$</sup>195<small>.99</small></div>
  <h4>Logo Design</h4>
  <ul><li>5 Custom Logo Design Concepts</li><li>By 2 Designers</li><li>Icon Design</li><li>All Final File Formats</li><li>Business Stationary</li><li>Business Card, Letterhead,</li><li>Envelope, Fax Template</li><li>MS Word Letterhead</li></ul>
  <span class="plan__scroll" style="right:20px;top:158px;height:222px"></span>
  <a class="btn" style="top:394px">See More</a>
</div>
<div class="plan plan--pro" style="left:441px;top:2294px;width:316px;height:498px;padding-top:34px">
  <div class="plan__pill">Pro Combo Package</div>
  <div class="plan__price"><sup>$</sup>950<small>.99</small></div>
  <h4>Logo Design</h4>
  <ul><li>5 Custom Logo Design Concepts</li><li>By 2 Designers</li><li>Icon Design</li><li>All Final File Formats</li><li>Business Stationary</li><li>Business Card, Letterhead,</li><li>Envelope, Fax Template</li><li>MS Word Letterhead</li><li>Dedicated designer</li><li>Logo Design</li></ul>
  <span class="plan__scroll" style="right:36px;top:156px;height:222px"></span>
  <a class="btn btn--outline" style="top:448px;border-color:#fff;background:var(--orange);color:#fff">See More</a>
</div>
<div class="plan" style="left:784px;top:2315px;width:289px;height:455px;padding-top:32px">
  <div class="plan__pill">Elite Combo Package</div>
  <div class="plan__price"><sup>$</sup>250<small>.99</small></div>
  <h4>Logo Design</h4>
  <ul><li>5 Custom Logo Design Concepts</li><li>By 2 Designers</li><li>Icon Design</li><li>All Final File Formats</li><li>Business Stationary</li><li>Business Card, Letterhead,</li><li>Envelope, Fax Template</li><li>MS Word Letterhead</li></ul>
  <span class="plan__scroll" style="right:20px;top:158px;height:222px"></span>
  <a class="btn" style="top:394px">See More</a>
</div>

<!-- cta -->
<div class="abs cta-band"></div>
<div class="cta">
  <h2>Need It solution &amp;<br>services consultation?</h2>
  <p>It is a long established fact that a reader will be distracted by the readable content of a page when looking It is a long established fact that a reader will be distracted by the readable content of a page when looking</p>
</div>
<a class="btn btn--orange" style="left:125px;top:3158px;width:125px;height:32px">Get Solution</a>
<div class="photo" role="img" aria-label="White humanoid service robot" style="left:686px;top:2877px;width:388px;height:373px;background:linear-gradient(135deg,#3c4a57,#8d9aa5 45%,#e6eaee 60%,#2a333c);box-shadow:0 10px 30px rgba(0,0,0,.15)"></div>

<!-- contact -->
<div class="abs" style="left:193px;top:3377px;width:287px;height:300px;background:var(--orange);clip-path:polygon(0 0,100% 0,80% 30%,40% 30%,40% 100%,0 100%)"></div>
<div class="abs" style="left:781px;top:3784px;width:183px;height:187px;background:linear-gradient(180deg,var(--teal),var(--teal-dark))"></div>
<div class="abs" style="left:205px;top:3632px;width:14px;height:207px;background:var(--ink)"></div>
<div class="abs" style="left:937px;top:3496px;width:12px;height:94px;background:var(--grey)"></div>
<div class="abs contact-frame"></div>
<div class="abs center contact-kicker" style="left:248px;width:652px">CONTACT</div>
<div class="abs center contact-title" style="left:248px;width:652px">Get Connect with us</div>
<div class="field" style="left:300px;top:3578px;width:267px">Enter your first name</div>
<div class="field" style="left:584px;top:3578px;width:265px">Enter your last name</div>
<div class="field" style="left:300px;top:3629px;width:267px">Enter your email address</div>
<div class="field" style="left:584px;top:3629px;width:265px">Enter your Phone No.</div>
<div class="field" style="left:300px;top:3680px;width:549px;height:32px;padding-top:6px;display:flex;justify-content:space-between">Please select the service you want
  <svg width="14" height="14" viewBox="0 0 24 24"><path d="M4 8l8 8 8-8" stroke="#0e1a22" stroke-width="3" fill="none"/></svg></div>
<div class="field field--area" style="left:300px;top:3729px;width:549px">Message.........</div>
<a class="btn btn--teal" style="left:300px;top:3869px;width:124px;height:31px">Send</a>

<!-- footer -->
<div class="abs footer"></div>
<div class="fcol" style="left:165px;width:240px">
  <h5>Build with Corvane</h5>
  <p style="font-size:14.5px;line-height:18.5px">It is a long established fact that a reader will be distracted by the readable content of a page when looking</p>
  <div class="ico" style="margin-top:12px">
    <svg width="20" height="20" viewBox="0 0 24 24"><circle cx="12" cy="12" r="10" fill="#fff"/><path d="M12 6v6l4 2" stroke="#000" stroke-width="2" fill="none"/></svg>
    <span style="line-height:20px">Mon - Sat 8:00, 17:30<br>Sunday Closed</span>
  </div>
</div>
<div class="fcol" style="left:446px">
  <h5>Menu</h5>
  <p>Home<br>About<br>Services<br>Contact</p>
</div>
<div class="fcol" style="left:585px">
  <h5>Our Services</h5>
  <p>Project Management<br>Project Framework<br>Monitoring &amp; Control</p>
</div>
<div class="fcol" style="left:801px;width:220px">
  <h5>Office in IL</h5>
  <div class="ico"><svg width="18" height="20" viewBox="0 0 24 24" fill="#fff"><path d="M12 2a7 7 0 0 0-7 7c0 5 7 13 7 13s7-8 7-13a7 7 0 0 0-7-7zm0 9.5A2.5 2.5 0 1 1 12 6.5a2.5 2.5 0 0 1 0 5z"/></svg><span>1450 Lakeshore Ave,<br>Evanston, IL 60201</span></div>
  <div class="ico"><svg width="18" height="18" viewBox="0 0 24 24" fill="#fff"><path d="M6.6 10.8c1.4 2.8 3.8 5.1 6.6 6.6l2.2-2.2c.3-.3.7-.4 1-.2 1.1.4 2.3.6 3.6.6.6 0 1 .4 1 1V20c0 .6-.4 1-1 1C10.6 21 3 13.4 3 4c0-.6.4-1 1-1h3.5c.6 0 1 .4 1 1 0 1.3.2 2.5.6 3.6.1.3 0 .7-.2 1z"/></svg><span>+ (555) 0142-300-1100<br>+ (555) 0142-300-1101</span></div>
  <div class="ico"><svg width="18" height="16" viewBox="0 0 24 20" fill="#fff"><path d="M2 2h20v16H2z"/><path d="M2 2l10 8 10-8" stroke="#000" stroke-width="2" fill="none"/></svg><span>info@corvane.io<br>support@corvane.io</span></div>
</div>
<div class="abs footer-bar"></div>
<div class="abs footer-logo"><i></i>CORVANE</div>
<div class="abs copyright">© 2013 <u>CORVANE</u> All Rights Reserved</div>

</body>
</html>
```